DPM Marketing Postcard

Design a 2 Sided marketing postcard for our Real estate management caompany. Looking for a professional yet fresh look that will be printed on a 6"x9" glossy flier

Contact information is www.dunkeldmanagement-example.com dunkeldmanagement@dunkeldmail-example.com and 312-480-7193

WE are targeting small condo and town home properties to take on their administrative responsibilities of management

```html
<!DOCTYPE html>
<html lang="en">
<head>
<meta charset="utf-8">
<title>DPM Marketing Postcard</title>
<link href="https://fonts.googleapis.com/css2?family=Open+Sans:wght@400;600;700;800&display=swap" rel="stylesheet">
<style>
  :root{
    --page:#8c8c8c;
    --card-top:#555657;
    --card-bottom:#353637;
    --red:#e4161d;
    --white:#ffffff;
    --text-soft:#e6e6e6;
    --photo-light:#eef3f8;
    --photo-mid:#c9d7e6;
    --photo-deep:#9fb4cb;
  }
  *{margin:0;padding:0;box-sizing:border-box}
  html,body{width:672px;height:1200px;overflow:hidden}
  body{background:var(--page);font-family:"Open Sans",Arial,sans-serif;color:var(--white);position:relative}

  .postcard{position:absolute;left:36px;width:600px;height:400px;overflow:hidden;
    background:linear-gradient(180deg,var(--card-top),var(--card-bottom));
    box-shadow:0 4px 14px rgba(0,0,0,.35)}
  .postcard--front{top:170px}
  .postcard--back{top:590px}

  /* FRONT */
  .hero-ring{position:absolute;left:0;top:0;width:600px;height:400px}
  .front-title{position:absolute;left:24px;top:28px;font-size:21px;font-weight:800;line-height:1.22;letter-spacing:.2px}
  .benefits{position:absolute;left:24px;top:100px;list-style:none}
  .benefits li{position:relative;padding-left:16px;font-size:10.5px;line-height:13.5px;margin-bottom:11px;color:var(--text-soft);white-space:nowrap}
  .benefits li::before{content:"";position:absolute;left:1px;top:2px;width:5px;height:9px;
    border-right:2px solid var(--red);border-bottom:2px solid var(--red);transform:rotate(40deg)}
  .benefits strong{color:var(--white);font-weight:800}
  .front-cta{position:absolute;left:24px;top:334px}
  .cta-line{font-size:16px;font-weight:800;letter-spacing:.2px;line-height:1.3}
  .cta-line .phone{font-size:21px}
  .web{font-size:15.5px;font-weight:400;line-height:1.3}
  .web b{font-weight:700}

  .price-badge{position:absolute;left:300px;top:266px;width:112px;height:112px;border-radius:50%;
    background:var(--red);border:3px solid var(--white);box-shadow:0 3px 6px rgba(0,0,0,.35);
    display:flex;flex-direction:column;align-items:center;justify-content:center;text-align:center;
    font-weight:800;font-size:12.5px;line-height:1.05}
  .price-badge .amount{font-size:21px;line-height:1.1}

  /* BACK */
  .back-title{position:absolute;left:0;right:0;top:14px;text-align:center;font-size:20px;font-weight:800;letter-spacing:.2px}
  .tagline-band{position:absolute;left:36px;right:36px;top:46px;height:22px;background:var(--red);
    font-size:11px;font-weight:600;text-align:center;line-height:22px}
  .column{position:absolute;top:82px;width:250px}
  .column--left{left:36px}
  .column--right{left:310px}
  .column h2{font-size:13.5px;font-weight:800;margin-bottom:8px}
  .column h2.spaced{margin-top:4px}
  .points{list-style:none}
  .points li{position:relative;padding-left:16px;font-size:10px;line-height:1.3;color:var(--text-soft);margin-bottom:8px}
  .points li::before{content:"";position:absolute;left:4px;top:4px;border-left:5px solid var(--red);
    border-top:3px solid transparent;border-bottom:3px solid transparent}
  .back-footer{position:absolute;left:0;right:0;top:342px;text-align:center}
  .back-footer .cta-line{font-size:17px}
  .back-footer .cta-line .phone{font-size:22px}
  .back-footer .contacts{font-size:12.5px;margin-top:1px}
</style>
</head>
<body>

<section class="postcard postcard--front">
  <svg class="hero-ring" viewBox="0 0 600 400">
    <defs>
      <linearGradient id="heroTone" x1="0" y1="0" x2="1" y2="1">
        <stop offset="0" stop-color="var(--photo-light)"/>
        <stop offset=".55" stop-color="var(--photo-mid)"/>
        <stop offset="1" stop-color="var(--photo-deep)"/>
      </linearGradient>
    </defs>
    <circle cx="515" cy="240" r="205" fill="var(--red)"/>
    <circle cx="519" cy="240" r="194" fill="var(--white)"/>
    <circle cx="522" cy="240" r="189" fill="url(#heroTone)" role="img"
      aria-label="Photo of a smiling businesswoman in a grey suit holding out keys and a blue folder, over faint architectural plans"/>
  </svg>

  <h1 class="front-title">DUNKELD PROPERTY<br>MANAGEMENT LLC (“DPM”)</h1>
  <ul class="benefits">
    <li>Cost effective property management solution<br>for 3-10 unit buildings</li>
    <li>Utilize our economies of scale to reduce costs across<br>existing services (trash, insurance, maintenance, etc)</li>
    <li>liminate the unfair burden placed on a few owners<br>to do all the work while others <strong>FREE-RIDE</strong></li>
    <li>Improve communication amongst all owners and<br>board members</li>
    <li>The association’s board of directors maintain all<br>decision-making power</li>
    <li>Utilize our vetted service providers for prompt<br>job completion and fair pricing</li>
  </ul>
  <div class="front-cta">
    <p class="cta-line">CALL US TODAY <span class="phone">312-480-7193</span></p>
    <p class="web">www.<b>dunkeldmanagement-example</b>.com</p>
  </div>

  <div class="price-badge">
    <span>PRICES</span><span>STARTING</span><span>AS LOW AS</span>
    <span class="amount">$100/</span><span>MONTH</span>
  </div>
</section>

<section class="postcard postcard--back">
  <h1 class="back-title">DUNKELD PROPERTY MANAGEMENT LLC (“DPM”)</h1>
  <p class="tagline-band">Improve compliance, reporting, and communication amongst all owners and board member</p>

  <div class="column column--left">
    <h2>WHO WE ARE:</h2>
    <ul class="points">
      <li>A professional services organization with a focus on small (3-10 unit) residential buildings</li>
      <li>Over 30 years of combined experience in real estate and property management</li>
      <li>Professional, courteous, timely service that is technologically driven</li>
    </ul>
    <h2 class="spaced">WHY USE DPM?</h2>
    <ul class="points">
      <li>Owners are rarely suited to manage associations and the burden often falls unfairly on one or two individuals to do all the work</li>
      <li>Low monthly fees tailored to your needs</li>
      <li>The association’s board of directors maintains control of all decision making</li>
    </ul>
  </div>

  <div class="column column--right">
    <h2>WHAT WE DO:</h2>
    <ul class="points">
      <li>Remove the administrative burden of managing small residential buildings</li>
      <li>Utilize economies of scale to reduce expenses for all owners across a wide variety of service providers</li>
      <li>Collect all assessments and pay all bills</li>
      <li>Provide monthly accounting reconciliation and reporting</li>
      <li>Issue 1099s to all contractors as required by law</li>
      <li>Prepare year-end financial statement</li>
      <li>Lender and legal HOA documents for mortgage companies and sales</li>
    </ul>
  </div>

  <div class="back-footer">
    <p class="cta-line">CALL US TODAY <span class="phone">312-480-7193</span></p>
    <p class="contacts">www.<b>dunkeldmanagement-example</b>.com | dunkeldmanagement@dunkeldmail-example.com</p>
  </div>
</section>

</body>
</html>
```